Exclusive beauty salon needs a price list or services booklet

I need a new very attractive flyer for my beauty salon, containing information on the different services and their prices.
In attachment you can find a pdf of the "old" one, but I'd love to have a beautifully designed new one!
I'd love to have a booklet in format 148 x 148 mm, or in US format, containing 12 or 16 pages, but if you can offer other nice looking designs they are welcome!
The services that need to come in the booklet with their prices can all be found on my website: www.atelierv.be, starting with
Gelaatsverzorging
Wimperverlenging
Suikerontharing
Wimperlifting
Permanente Make Up
Airbrush Tanning

Target Market(s)

woman from 20 to 89 years old

Industry/Entity Type

Beauty Salon

Font styles to use
Sans Serif

Colors

Designer to choose colors to be used in the design.

Requirements
Must have
• a classy nice look, it must contain details about the services from my beauty salon and their prices, and nice pictures.
• The Names, prices and explanations of the services can easily be found on my website: www.atelierv.be
Nice to have
• In attachment you can find the "old" price list in pdf, what I need now is a "new booklet" with the new logo and updated services price list.
• I need a very nice and attractive looking booklet, classy chique, Paris chique, looking very expensive.
Should not have
• Not too much colors, not too curly, but still feminine

```html
<!DOCTYPE html>
<html lang="nl">
<head>
<meta charset="utf-8">
<title>Atelier V – Prijslijst</title>
<link href="https://fonts.googleapis.com/css2?family=Questrial&display=swap" rel="stylesheet">
<style>
  :root {
    --stage: #e6e3e4;
    --ink: #222222;
    --ink-soft: #3a3a3a;
    --blush: #f8dfe4;
    --peach: #f6d6c6;
    --peach-light: #fbe9df;
    --sky: #9fd6e6;
    --teal: #55c2c6;
    --pill: #f2a7ad;
    --white: #ffffff;
  }
  * { box-sizing: border-box; margin: 0; padding: 0; }
  html, body { width: 1200px; height: 1200px; overflow: hidden; }
  body {
    background: var(--stage);
    font-family: "Questrial", "Century Gothic", sans-serif;
    color: var(--ink);
    position: relative;
  }
  .page {
    position: absolute;
    width: 504px;
    height: 504px;
    overflow: hidden;
    background: var(--white);
    box-shadow: 0 4px 14px rgba(0,0,0,0.18);
  }
  .brand-name {
    display: flex; align-items: center; gap: 8px;
    color: var(--ink); font-weight: 400; letter-spacing: 0;
  }
  .brand-name .dot {
    width: 8px; height: 8px; border-radius: 50%; background: var(--ink); flex: none;
  }

  /* Front cover */
  .cover { left: 66px; top: 78px; }
  .cover-backdrop {
    position: absolute; inset: 0;
    background:
      radial-gradient(circle at 15% 25%, #fbe5ea 0 18%, transparent 40%),
      radial-gradient(circle at 10% 75%, #f6d0d8 0 14%, transparent 38%),
      radial-gradient(circle at 55% 5%, #f9dbe1 0 10%, transparent 30%),
      linear-gradient(135deg, var(--blush) 0%, #fbe9ec 55%, #fdf0f2 100%);
  }
  .portrait-ring {
    position: absolute; left: 100px; top: 66px;
    width: 304px; height: 304px; border-radius: 50%;
    border: 3px solid var(--sky);
    background: var(--white);
    overflow: hidden;
  }
  .portrait-ring .photo {
    position: absolute; inset: 8px; border-radius: 50%;
    background: radial-gradient(circle at 55% 45%, #efd3c4 0%, #e2b9a4 45%, #fdf7f5 80%);
  }
  .cover .brand-name {
    position: absolute; left: 0; right: 0; top: 440px;
    justify-content: center; font-size: 22px;
  }

  /* Back cover */
  .back { left: 637px; top: 78px; }
  .back-backdrop {
    position: absolute; inset: 0;
    background:
      radial-gradient(circle at 15% 12%, #f6c6d3 0 9%, transparent 22%),
      radial-gradient(circle at 90% 30%, #f5bccb 0 8%, transparent 24%),
      radial-gradient(circle at 95% 85%, #f0a9bd 0 7%, transparent 22%),
      radial-gradient(circle at 45% 50%, #ffffff 0 30%, transparent 62%),
      linear-gradient(135deg, #ecd3ea 0%, #f8eef6 45%, #f1dcec 100%);
  }
  .back .brand-name {
    position: absolute; left: 76px; top: 282px; font-size: 13px; gap: 6px;
  }
  .back .brand-name .dot { width: 6px; height: 6px; }
  .contact {
    position: absolute; left: 68px; top: 320px;
    list-style: none; font-size: 12.5px; line-height: 17px; color: var(--ink);
  }
  .contact li { display: flex; align-items: flex-start; gap: 8px; }
  .contact svg { width: 9px; height: 9px; margin-top: 4px; flex: none; fill: var(--teal); }
  .back-band {
    position: absolute; left: 0; top: 444px; width: 382px; height: 13px;
    background: var(--sky);
  }
  .back-foot {
    position: absolute; left: 0; top: 457px; width: 360px; height: 47px;
    background: linear-gradient(90deg, var(--white) 70%, rgba(255,255,255,0));
  }

  /* Inside spread */
  .inside { left: 334px; top: 667px; }
  .inside-header {
    position: absolute; left: 0; top: 0; width: 504px; height: 178px;
    background:
      radial-gradient(ellipse at 22% 55%, #f1c9b5 0 20%, transparent 45%),
      radial-gradient(circle at 85% 20%, #fbe4d9 0 14%, transparent 35%),
      linear-gradient(90deg, var(--peach) 0%, var(--peach-light) 100%);
  }
  .inside-title {
    position: absolute; left: 194px; top: 72px;
    font-size: 32px; font-weight: 400; color: var(--ink);
  }
  .services { position: absolute; left: 30px; top: 194px; width: 268px; }
  .service { margin-bottom: 10px; }
  .service-head { display: flex; justify-content: space-between; align-items: center; margin-bottom: 4px; }
  .service-name { font-size: 11.5px; font-weight: 400; color: var(--teal); }
  .price {
    background: var(--pill); color: var(--white);
    font-size: 12px; line-height: 14px; padding: 0 8px; border-radius: 8px;
  }
  .service p { font-size: 9.6px; line-height: 11.6px; color: var(--ink-soft); text-align: justify; }
  .service.flash { margin-top: 20px; }
  .feature-photo {
    position: absolute; width: 128px; height: 128px; border-radius: 50%;
    border: 3px solid var(--sky); background: var(--white); overflow: hidden;
  }
  .feature-photo .photo { position: absolute; inset: 6px; border-radius: 50%; }
  .feature-photo.face { left: 351px; top: 198px; }
  .feature-photo.face .photo { background: radial-gradient(circle at 55% 40%, #f4d8cc 0%, #e6bba8 50%, #f5f3f3 85%); }
  .feature-photo.products { left: 351px; top: 350px; }
  .feature-photo.products .photo { background: linear-gradient(90deg, #fdf6f6 0%, #f3b9be 30%, #fbf4f4 50%, #b8e1bd 70%, #f6fbf6 100%); }
</style>
</head>
<body>

<section class="page cover" aria-label="Voorkant">
  <div class="cover-backdrop" role="img" aria-label="Zachtroze bloesemtakken als achtergrond"></div>
  <div class="portrait-ring">
    <div class="photo" role="img" aria-label="Portretfoto van een vrouw met opgestoken haar"></div>
  </div>
  <div class="brand-name"><span class="dot"></span><span>Atelier V</span></div>
</section>

<section class="page back" aria-label="Achterkant">
  <div class="back-backdrop" role="img" aria-label="Roze bloesemknoppen op takken, zacht vervaagd"></div>
  <div class="brand-name"><span class="dot"></span><span>Atelier V</span></div>
  <ul class="contact">
    <li><svg viewBox="0 0 10 10"><path d="M2 0.5 L3.6 2.6 L2.8 3.6 Q4 6 6.4 7.2 L7.4 6.4 L9.5 8 L8.6 9.5 Q2 8.5 0.5 1.4 Z"/></svg><span>0470 31 62 54</span></li>
    <li><svg viewBox="0 0 10 10"><circle cx="5" cy="5" r="4.5"/></svg><span>www.atelierv.be</span></li>
    <li><svg viewBox="0 0 10 10"><path d="M0.5 3 L5 0.5 L9.5 3 L9.5 9 L0.5 9 Z"/></svg><span>vera@atelierv.be</span></li>
    <li><svg viewBox="0 0 10 10"><path d="M5 0.5 A3.3 3.3 0 0 1 8.3 3.8 Q8.3 6 5 9.5 Q1.7 6 1.7 3.8 A3.3 3.3 0 0 1 5 0.5 Z"/></svg><span>Atelier V Schoonheidsinstituut<br>Lindenlaan 14 (2e verdieping<br>Rozenhof) 9000 GENT</span></li>
  </ul>
  <div class="back-band"></div>
  <div class="back-foot"></div>
</section>

<section class="page inside" aria-label="Binnenpagina">
  <div class="inside-header" role="img" aria-label="Vrouw met opgestoken haar en open hand voor een perzikkleurige bloesemachtergrond"></div>
  <h1 class="inside-title">Gelaatsverzorging</h1>

  <div class="services">
    <article class="service">
      <div class="service-head"><h2 class="service-name">Cosmetische Verzorging</h2><span class="price">€30</span></div>
      <p>Verzorging i.o.v. Dermatoloog.<br>De verzorging bestaat uit: oppervlakkige reiniging, verwijderen zwarte puntjes en onzuiverheden, zuiverend masker.</p>
    </article>
    <article class="service">
      <div class="service-head"><h2 class="service-name">Hydratation Essentielle</h2><span class="price">€15</span></div>
      <p>Voor een gehydrateerde, volle en frisse huid.<br>Geschikt voor alle huidtypes.<br>De verzorging bestaat uit: epilatie wenkbrauwen, oppervlakkige reiniging, diepe reiniging, verwijderen van comedonen, massage van gelaat en décolleté, instituutmasker aangepast aan huidconditie, serum, dagcème, handmassage.</p>
    </article>
    <article class="service flash">
      <div class="service-head"><h2 class="service-name">Flash Nettoyant</h2><span class="price">€59 - 50 min.</span></div>
      <p>Voor een gehydrateerde en comfortabele huid.<br>Voor alle huidtypes, bij een vermoeide huid met weinig uitstraling.<br>De verzorging bestaat uit: epilatie wenkbrauwen, oppervlakkige reiniging, diepe reiniging, crememasker aangepast aan huidconditie, serum, dagcème, handmassage.</p>
    </article>
  </div>

  <div class="feature-photo face"><div class="photo" role="img" aria-label="Glimlachende vrouw die haar wang aanraakt"></div></div>
  <div class="feature-photo products"><div class="photo" role="img" aria-label="Twee flesjes gezichtswater, roze en groen"></div></div>
</section>

</body>
</html>
```